Veltana corporate website

Dear graphic designers,
We would like to create a brand new corporate website for our company named "Veltana".
Veltana is a small Swiss premium IT company, with very prestigious clients in the Private Banking industry.
Here would be the values which could be associated to Veltana: trustworthy, serious, modern, high tech, high quality, sobriety, elegant.
Please find attached the Veltana logo in SVG format.
Our new website will have for only purpose to present briefly the company in one page: the team of experts (4 employees), the mission, the expertise and the contact info.
Very short and concise, easy to read.
Like this website for example but even shorter: https://www.dorimel-example.com/

```html
<!DOCTYPE html>
<html lang="en">
<head>
<meta charset="utf-8">
<title>Veltana</title>
<link rel="stylesheet" href="https://fonts.googleapis.com/css2?family=Ubuntu:wght@400;500;700&family=Lato:wght@400;700&display=swap">
<style>
:root{
  --blue-deep:#0f4fa8;
  --blue:#0d6eb8;
  --blue-light:#7fb0df;
  --blue-pale:#a9c9ea;
  --blue-mist:#eaf2fb;
  --ink:#111418;
  --text:#333;
  --white:#fff;
  --black:#000;
}
*{box-sizing:border-box;margin:0;padding:0}
html,body{width:1200px;height:3765px;overflow:hidden;background:var(--white)}
body{position:relative;font-family:'Lato',sans-serif;color:var(--text)}
a{color:inherit;text-decoration:none}
.abs{position:absolute}
h1,h2,h3,h4,.brand,.btn{font-family:'Ubuntu',sans-serif}

/* header */
.site-header{left:0;top:0;width:1200px;height:85px;background:var(--white)}
.brand{font-weight:500;letter-spacing:3px;text-transform:uppercase;white-space:nowrap}
.header-brand{left:98px;top:20px;font-size:40px;color:var(--blue-deep)}
.nav a{position:absolute;top:31px;font-size:15px;color:#222;white-space:nowrap}
.nav-ring{left:526px;top:11px;width:68px;height:62px;border:4px solid var(--blue-deep);border-radius:50%}

/* hero */
.hero-photo{left:0;top:85px;width:1200px;height:598px;background:radial-gradient(ellipse at 75% 45%,#c9d6e2 0%,#6f8aa3 30%,#1f3d58 60%,#0b1a2b 100%)}
.hero-disc{left:68px;top:146px;width:474px;height:474px;border-radius:50%;background:var(--blue-deep)}
.hero-disc-inner{left:90px;top:168px;width:430px;height:430px;border-radius:50%;background:#6fa3d8}
.hero-welcome{left:90px;top:282px;width:430px;text-align:center;font-family:'Ubuntu',sans-serif;font-size:29px;color:var(--ink)}
.hero-title{left:90px;top:312px;width:430px;text-align:center;font-size:74px;font-weight:700;color:var(--white);letter-spacing:2px}
.btn{display:flex;align-items:center;justify-content:center;border-radius:40px;color:var(--white);font-weight:500}
.hero-btn{left:209px;top:424px;width:194px;height:63px;background:var(--blue-deep);font-size:26px}

/* section titles */
.section-title{left:0;width:1200px;text-align:center;font-size:38px;font-weight:500;color:var(--ink)}
.title-rule{height:3px;background:var(--blue-deep)}

/* values */
.value-card{width:232px;height:225px;background:var(--white);border-radius:6px;box-shadow:0 3px 12px rgba(0,0,0,.12)}
.value-card.is-active{border:2px solid var(--blue-deep)}
.value-card svg{position:absolute;left:56px;top:20px}
.value-card .label{position:absolute;left:0;top:171px;width:100%;text-align:center;font-family:'Ubuntu',sans-serif;font-weight:500;font-size:19px;color:var(--ink)}

/* bands */
.band{left:0;width:1200px}
.band-mission{top:1584px;height:535px;background:linear-gradient(180deg,#1a80c6 0%,#1272b8 55%,#2d7ebd 100%)}
.band-expertise{top:2779px;height:532px;background:linear-gradient(180deg,#1c5db0 0%,#1a67b8 50%,#2a6fb8 100%)}
.photo-frame{background:var(--blue-pale)}
.photo.warm{background:linear-gradient(160deg,#dcdcdc,#c9a277 45%,#d08a3e 70%,#8a8f96)}
.photo.cool{background:linear-gradient(160deg,#c8cfd8,#e2c7a6 40%,#24365c 70%,#cfd3d8)}
.band-title{font-size:40px;font-weight:500;color:var(--white)}
.band-rule{height:3px;width:67px;background:var(--white)}
.band-copy{width:460px;font-size:16px;line-height:24px;color:var(--white);text-align:justify}
.btn-light{background:var(--blue-light);font-size:26px;font-weight:400}

/* team */
.team-card{width:237px;height:261px;border-radius:10px;background:var(--blue)}
.team-card.is-active{background:var(--blue-light)}
.avatar{position:absolute;left:71px;top:19px;width:94px;height:94px;border-radius:50%;background:linear-gradient(180deg,#e4e7ea,#8c96a3)}
.team-card h3{position:absolute;left:0;top:138px;width:100%;text-align:center;font-size:19px;font-weight:500;color:var(--white)}
.team-card p{position:absolute;left:14px;top:172px;width:209px;text-align:center;font-size:11.5px;line-height:20px;color:var(--white)}

/* footer */
.site-footer{left:0;top:3311px;width:1200px;height:454px;background:var(--black)}
.footer-brand{left:80px;top:3437px;font-size:38px;color:var(--blue)}
.social{width:14px;height:14px;border-radius:50%;background:var(--blue)}
.footer-heading{font-weight:500;font-size:20px;color:var(--white);letter-spacing:.5px}
.footer-link{left:341px;font-size:17px;color:var(--white)}
.contact-line{left:595px;width:230px;font-size:17px;line-height:23px;color:var(--white)}
.contact-icon{left:566px}
.field{border:1px solid #cfd6de;border-radius:6px;background:var(--black);font-family:'Lato',sans-serif;font-size:8px;color:var(--white);padding:14px 0 0 10px;text-transform:uppercase}
.submit{left:858px;top:3617px;width:148px;height:44px;border-radius:6px;background:var(--blue-light);color:var(--white);font-size:17px;display:flex;align-items:center;justify-content:center;gap:10px}
.footer-rule{left:89px;top:3686px;width:1022px;height:1px;background:#9aa}
.copyright{left:0;top:3705px;width:1200px;text-align:center;font-size:15px;color:var(--white)}
</style>
</head>
<body>

<header class="site-header abs">
  <div class="brand header-brand abs">Veltana</div>
  <nav class="nav">
    <span class="nav-ring abs"></span>
    <a style="left:541px">Home</a>
    <a style="left:615px">Team</a>
    <a style="left:685px">Services</a>
    <a style="left:774px">Company</a>
    <a style="left:872px">Projects</a>
    <a style="left:961px">Careers</a>
    <a style="left:1047px">Contact</a>
  </nav>
</header>

<section class="hero">
  <div class="hero-photo abs" role="img" aria-label="Smiling engineer holding a laptop in a server room"></div>
  <div class="hero-disc abs"></div>
  <div class="hero-disc-inner abs"></div>
  <p class="hero-welcome abs">WELCOME TO</p>
  <h1 class="hero-title abs">VELTANA</h1>
  <a class="btn hero-btn abs">Get Started</a>
</section>

<section class="values">
  <h2 class="section-title abs" style="top:758px">Our Values</h2>
  <div class="title-rule abs" style="left:578px;top:815px;width:44px"></div>

  <div class="value-card abs" style="left:101px;top:877px">
    <svg width="120" height="120" viewBox="0 0 120 120"><circle cx="60" cy="60" r="56" fill="#eaf2fb" stroke="#0f4fa8" stroke-width="3"/><path d="M44 36 L60 30 L76 36 V56 Q60 74 44 56 Z" fill="none" stroke="#111" stroke-width="2.5"/><path d="M52 50 L58 56 L69 44" fill="none" stroke="#111" stroke-width="2.5"/><path d="M36 84 H84" stroke="#111" stroke-width="2.5"/></svg>
    <span class="label">Trustworthy</span>
  </div>
  <div class="value-card is-active abs" style="left:355px;top:877px">
    <svg width="120" height="120" viewBox="0 0 120 120"><circle cx="60" cy="60" r="56" fill="#eaf2fb" stroke="#0f4fa8" stroke-width="3"/><rect x="34" y="38" width="24" height="16" rx="4" fill="none" stroke="#111" stroke-width="2.5"/><rect x="62" y="38" width="24" height="16" rx="4" fill="none" stroke="#111" stroke-width="2.5"/><path d="M40 82 H80 M48 72 H72" stroke="#111" stroke-width="2.5"/></svg>
    <span class="label">Serious</span>
  </div>
  <div class="value-card abs" style="left:611px;top:877px">
    <svg width="120" height="120" viewBox="0 0 120 120"><circle cx="60" cy="60" r="56" fill="#eaf2fb" stroke="#0f4fa8" stroke-width="3"/><circle cx="60" cy="56" r="20" fill="none" stroke="#111" stroke-width="2.5"/><path d="M40 56 H80 M60 36 Q70 56 60 76 Q50 56 60 36" fill="none" stroke="#111" stroke-width="2.5"/></svg>
    <span class="label">Modern</span>
  </div>
  <div class="value-card abs" style="left:867px;top:877px">
    <svg width="120" height="120" viewBox="0 0 120 120"><circle cx="60" cy="60" r="56" fill="#eaf2fb" stroke="#0f4fa8" stroke-width="3"/><rect x="42" y="48" width="36" height="28" rx="3" fill="none" stroke="#111" stroke-width="2.5"/><path d="M60 30 V44 M52 38 L60 30 L68 38 M48 84 H72" fill="none" stroke="#111" stroke-width="2.5"/></svg>
    <span class="label">High Tech</span>
  </div>
  <div class="value-card abs" style="left:229px;top:1162px">
    <svg width="120" height="120" viewBox="0 0 120 120"><circle cx="60" cy="60" r="56" fill="#eaf2fb" stroke="#0f4fa8" stroke-width="3"/><path d="M60 32 L67 48 L84 50 L71 61 L75 78 L60 69 L45 78 L49 61 L36 50 L53 48 Z" fill="none" stroke="#111" stroke-width="2.5"/></svg>
    <span class="label">High Quality</span>
  </div>
  <div class="value-card abs" style="left:484px;top:1162px">
    <svg width="120" height="120" viewBox="0 0 120 120"><circle cx="60" cy="60" r="56" fill="#eaf2fb" stroke="#0f4fa8" stroke-width="3"/><circle cx="60" cy="60" r="26" fill="none" stroke="#111" stroke-width="2.5"/><circle cx="60" cy="60" r="16" fill="none" stroke="#111" stroke-width="2.5"/></svg>
    <span class="label">Sobriety</span>
  </div>
  <div class="value-card abs" style="left:740px;top:1162px">
    <svg width="120" height="120" viewBox="0 0 120 120"><circle cx="60" cy="60" r="56" fill="#eaf2fb" stroke="#0f4fa8" stroke-width="3"/><path d="M36 38 H84 M40 44 H80 M44 44 V80 M54 44 V80 M66 44 V80 M76 44 V80 M38 84 H82" stroke="#111" stroke-width="2.5"/></svg>
    <span class="label">Elegant</span>
  </div>
  <svg class="abs" style="left:462px;top:1117px" width="12" height="16" viewBox="0 0 12 16"><path d="M1 1 L1 13 L4 10 L7 15 L9 14 L6 9 L10 9 Z" fill="#fff" stroke="#222" stroke-width="1"/></svg>
</section>

<section class="mission">
  <div class="band band-mission abs"></div>
  <div class="photo-frame abs" style="left:88px;top:1517px;width:453px;height:550px"></div>
  <div class="photo warm abs" style="left:98px;top:1503px;width:454px;height:552px" role="img" aria-label="Young professional smiling while working on a laptop"></div>
  <h2 class="band-title abs" style="left:604px;top:1622px">The Mission</h2>
  <div class="band-rule abs" style="left:604px;top:1683px"></div>
  <p class="band-copy abs" style="left:604px;top:1708px">Lorem ipsum dolor sit amet, consectetur adipiscing elit, sed do eiusmod tempor incididunt ut labore et dolore magna aliqua. Ut enim ad minim veniam, quis nostrud exercitation ullamco laboris nisi ut aliquip ex ea commodo consequat. Lorem ipsum dolor sit amet, consectetur adipiscing elit, sed do eiusmod tempor incididunt ut labore et dolore magna aliqua. Ut enim ad minim veniam, quis nostrud exercitation ullamco laboris nisi ut aliquip ex ea commodo consequat.Lorem ipsum dolor sit amet, consectetur adipiscing elit, sed do eiusmod tempor incididunt ut labore et dolore magna aliqua. Ut enim ad minim veniam, quis</p>
  <a class="btn btn-light abs" style="left:601px;top:1982px;width:196px;height:61px">Read More</a>
</section>

<section class="team">
  <h2 class="section-title abs" style="top:2213px">Our Team</h2>
  <div class="title-rule abs" style="left:571px;top:2276px;width:58px"></div>
  <div class="team-card abs" style="left:101px;top:2325px"><div class="avatar" role="img" aria-label="Portrait of team member"></div><h3>Nemo enim ipsam</h3><p>Lorem ipsum dolor sit amet, consectetur adipiscing elit, sed do eiusmod tempor incididunt ut labore</p></div>
  <div class="team-card is-active abs" style="left:355px;top:2325px"><div class="avatar" role="img" aria-label="Portrait of team member"></div><h3>Nemo enim ipsam</h3><p>Lorem ipsum dolor sit amet, consectetur adipiscing elit, sed do eiusmod tempor incididunt ut labore</p></div>
  <div class="team-card abs" style="left:611px;top:2325px"><div class="avatar" role="img" aria-label="Portrait of team member"></div><h3>Nemo enim ipsam</h3><p>Lorem ipsum dolor sit amet, consectetur adipiscing elit, sed do eiusmod tempor incididunt ut labore</p></div>
  <div class="team-card abs" style="left:865px;top:2325px"><div class="avatar" role="img" aria-label="Portrait of team member"></div><h3>Nemo enim ipsam</h3><p>Lorem ipsum dolor sit amet, consectetur adipiscing elit, sed do eiusmod tempor incididunt ut labore</p></div>
  <svg class="abs" style="left:464px;top:2601px" width="12" height="16" viewBox="0 0 12 16"><path d="M1 1 L1 13 L4 10 L7 15 L9 14 L6 9 L10 9 Z" fill="#fff" stroke="#222" stroke-width="1"/></svg>
</section>

<section class="expertise">
  <div class="band band-expertise abs"></div>
  <div class="photo-frame abs" style="left:659px;top:2711px;width:455px;height:553px"></div>
  <div class="photo cool abs" style="left:647px;top:2697px;width:455px;height:554px" role="img" aria-label="Smiling businesswoman using a tablet in an office"></div>
  <h2 class="band-title abs" style="left:101px;top:2817px">The Expertise</h2>
  <div class="band-rule abs" style="left:101px;top:2877px"></div>
  <p class="band-copy abs" style="left:101px;top:2903px">Lorem ipsum dolor sit amet, consectetur adipiscing elit, sed do eiusmod tempor incididunt ut labore et dolore magna aliqua. Ut enim ad minim veniam, quis nostrud exercitation ullamco laboris nisi ut aliquip ex ea commodo consequat. Lorem ipsum dolor sit amet, consectetur adipiscing elit, sed do eiusmod tempor incididunt ut labore et dolore magna aliqua. Ut enim ad minim veniam, quis nostrud exercitation ullamco laboris nisi ut aliquip ex ea commodo consequat.Lorem ipsum dolor sit amet, consectetur adipiscing elit, sed do eiusmod tempor incididunt ut labore et dolore magna aliqua. Ut enim ad minim veniam, quis</p>
  <a class="btn btn-light abs" style="left:99px;top:3176px;width:196px;height:62px">Read More</a>
</section>

<footer>
  <div class="site-footer abs"></div>
  <div class="brand footer-brand abs">Veltana</div>
  <span class="social abs" style="left:96px;top:3512px"></span>
  <span class="social abs" style="left:133px;top:3512px"></span>
  <span class="social abs" style="left:179px;top:3512px"></span>
  <span class="social abs" style="left:223px;top:3512px"></span>
  <span class="social abs" style="left:268px;top:3512px"></span>

  <h4 class="footer-heading abs" style="left:341px;top:3358px">USEFUL LINKS</h4>
  <a class="footer-link abs" style="top:3416px">Home</a>
  <a class="footer-link abs" style="top:3443px">Team</a>
  <a class="footer-link abs" style="top:3470px">Services</a>
  <a class="footer-link abs" style="top:3497px">Company</a>
  <a class="footer-link abs" style="top:3525px">Projects</a>
  <a class="footer-link abs" style="top:3553px">Careers</a>
  <a class="footer-link abs" style="top:3579px">Contact</a>

  <h4 class="footer-heading abs" style="left:566px;top:3358px">CONTACT US</h4>
  <svg class="contact-icon abs" style="top:3414px" width="12" height="16" viewBox="0 0 12 16"><path d="M6 0 A6 6 0 0 1 12 6 C12 10 6 16 6 16 C6 16 0 10 0 6 A6 6 0 0 1 6 0 Z" fill="#fff"/><circle cx="6" cy="6" r="2.2" fill="#000"/></svg>
  <p class="contact-line abs" style="top:3411px;width:200px">Lorem ipsum dolor sit amet, consectetur adipiscing elit,</p>
  <svg class="contact-icon abs" style="top:3517px" width="14" height="14" viewBox="0 0 14 14"><path d="M3 0 L5.5 3.5 L4 5.5 Q5.5 8.5 8.5 10 L10.5 8.5 L14 11 L12 14 Q1 13 0 2 Z" fill="#fff"/></svg>
  <p class="contact-line abs" style="top:3513px">+41 22 555 0142</p>
  <svg class="contact-icon abs" style="top:3574px" width="16" height="12" viewBox="0 0 16 12"><rect width="16" height="12" rx="1" fill="#fff"/><path d="M0 1 L8 7 L16 1" fill="none" stroke="#000" stroke-width="1.4"/></svg>
  <p class="contact-line abs" style="top:3569px">info@veltana-example.com</p>

  <h4 class="footer-heading abs" style="left:849px;top:3358px">CONTACT INFO</h4>
  <div class="field abs" style="left:851px;top:3413px;width:117px;height:32px">Name</div>
  <div class="field abs" style="left:984px;top:3413px;width:117px;height:32px">Email</div>
  <div class="field abs" style="left:852px;top:3461px;width:249px;height:34px">Phone Number</div>
  <div class="field abs" style="left:852px;top:3509px;width:249px;height:88px">Message</div>
  <div class="submit abs">Submit Now
    <svg width="14" height="14" viewBox="0 0 14 14"><circle cx="7" cy="7" r="7" fill="#fff"/><path d="M4 7 H9.5 M7 4.5 L9.5 7 L7 9.5" fill="none" stroke="#7fb0df" stroke-width="1.8"/></svg>
  </div>

  <div class="footer-rule abs"></div>
  <p class="copyright abs">© 2023 Veltana. All Rights Reserved.</p>
</footer>

</body>
</html>
```